Brochure Design Project

We need a brochure designed for our company, specifically targeted at our corporate business customers ... Banks, Financial Services, Government. The brochure needs to detail our services and what we have to offer.

It may be a brochure/booklet that we can give to clients when we meet them. It needs to have a very corporate look and feel and needs to align with our colour palette and logo.

Information is held on our website www.tessaroworldservices.com
Updates

Thank you everyone for being part of this project.  It was a very hard decision.

Target Market(s)

Corporate business and clients including banks, financial services, insurance and government.

Industry/Entity Type

Business

Requirements
Must have
• Must have a corporate and global feel to it.
Must have our logo and same or similar colour palette.

```html
<!DOCTYPE html>
<html lang="en">
<head>
<meta charset="utf-8">
<title>Tessaro World Services – Corporate Brochure</title>
<link href="https://fonts.googleapis.com/css2?family=Michroma&family=Open+Sans:ital,wght@0,400;0,700;1,700&family=Tinos:wght@400;700&display=swap" rel="stylesheet">
<style>
:root{
  --navy:#071d45;
  --deep:#0b2f6b;
  --blue:#1b5fae;
  --sky:#3f93db;
  --ice:#cfe3f6;
  --ink:#1a1a1a;
  --paper:#ffffff;
  --backdrop:#ffffff;
  --frame:#cfcfcf;
}
*{box-sizing:border-box;margin:0;padding:0}
html,body{width:990px;height:1200px;overflow:hidden;background:var(--backdrop)}
.canvas{position:relative;width:990px;height:1200px;border:1px solid var(--frame)}
.spread{position:absolute;left:163px;width:784px;height:450px;background:var(--paper);box-shadow:0 4px 10px rgba(0,0,0,.35)}
.spread--outer{top:120px}
.spread--inner{top:620px}
.page{position:absolute;top:0;width:392px;height:450px;overflow:hidden}
.page--left{left:0}
.page--right{left:392px;border-left:1px solid #e3e3e3}
.band{position:absolute;left:0;width:100%}
.flow{position:absolute;display:flex;flex-direction:column;align-items:flex-start;z-index:1}
.body-copy{font-family:"Tinos",serif;font-size:7.2px;line-height:1.25;color:var(--ink)}
.body-copy p{margin-bottom:3px}
.body-copy ul{list-style:none;padding-left:8px;margin-bottom:3px}
.row{display:flex;gap:8px;align-items:flex-start;width:100%}
.brand{position:absolute;display:flex;flex-direction:column;align-items:center;font-family:"Open Sans",sans-serif;font-weight:700;color:var(--deep);text-align:center;z-index:1}
.brand__mark{border-radius:50%;background:var(--deep)}
.brand__name{letter-spacing:.5px;line-height:1.05}
.brand__tag{font-weight:700;color:var(--deep);white-space:nowrap}
.section-title{display:inline-flex;align-items:center;white-space:nowrap;font-family:"Michroma",sans-serif;color:#fff;text-transform:uppercase;height:20px;font-size:9.5px;padding:0 16px 0 12px;border-radius:0 10px 10px 0;background:linear-gradient(180deg,var(--sky),var(--deep) 60%,var(--navy));box-shadow:0 2px 3px rgba(0,0,0,.3)}
.section-title--box{border-radius:6px;border:2px solid var(--ice);padding:0 12px 0 10px;font-size:9px;height:19px}
.photo{position:relative;flex:none;border:1px solid #dbe6f2}
.photo-label{position:absolute;left:4px;bottom:4px;font-family:"Open Sans",sans-serif;font-size:5.5px;color:#fff;background:rgba(7,29,69,.8);padding:1px 4px;white-space:nowrap}
.url{position:absolute;font-family:"Open Sans",sans-serif;font-size:6px;color:#fff;z-index:1}
.headline{font-family:"Michroma",sans-serif;font-size:10.5px;line-height:1.4;color:var(--navy);text-transform:uppercase;border-bottom:2px solid #bfc8d4;padding-bottom:1px;white-space:nowrap}
.tagline{position:absolute;font-family:"Open Sans",sans-serif;font-style:italic;font-weight:700;font-size:11.5px;line-height:1.25;color:#fff}
.contact{position:absolute;left:222px;top:346px;width:140px;height:66px;border-radius:6px;border:1.5px solid var(--ice);background:linear-gradient(180deg,var(--blue),var(--navy));color:#fff;text-align:center;font-family:"Tinos",serif;font-size:5.4px;line-height:1.3;padding-top:3px;z-index:2}
.contact__title{font-family:"Michroma",sans-serif;font-size:9px;margin-bottom:3px}
</style>
</head>
<body>
<div class="canvas">

  <!-- Outer spread: back page and cover -->
  <section class="spread spread--outer">
    <div class="page page--left">
      <svg class="band" style="top:0" width="392" height="40" viewBox="0 0 392 40" aria-hidden="true">
        <path d="M0 0H392V14H300C240 14 230 22 170 22H0Z" fill="var(--deep)"/>
        <path d="M100 22C170 22 230 10 300 10H392V18H300C240 18 200 30 120 30Z" fill="var(--sky)"/>
        <path d="M300 24H392V28H300Z" fill="var(--blue)"/>
      </svg>
      <div class="brand" style="left:10px;top:30px;width:60px">
        <span class="brand__mark" style="width:14px;height:14px"></span>
        <span class="brand__name" style="font-size:6.5px;margin-top:2px">TESSARO</span>
        <span class="brand__tag" style="font-size:3.6px">WORLD SERVICES</span>
      </div>
      <div class="flow" style="left:20px;top:62px;width:352px">
        <div class="body-copy">
          <p>Our approach to problem solving is holistic ensuring that the 'whole' system is understood and managed. We have found that if you impact one thing, you impact everything; therefore sustainable solutions for our Global Community must encompass all aspects of the community.Our approach to solutions is based on</p>
          <ul>
            <li>A multi-dimensional view of the problem</li>
            <li>Understanding the "whole" system to ensure all impacts are managed</li>
            <li>The belief that everything is connected and therefore ALL need to be accounted for within the change</li>
          </ul>
          <p style="margin-top:5px">We believe in</p>
          <ul>
            <li>Designing and delivering sustainable solutions</li>
            <li>Utilising an holistic approach in all we do</li>
            <li>Working collaboratively with all our partners</li>
            <li>Creating a new way of operating through our leading edge programs</li>
            <li>Delivering programs that create unity and alignment with the vision and strategy</li>
            <li>Supporting the community and environment</li>
          </ul>
        </div>
        <div class="row" style="margin:4px 0 0 -14px;width:380px;gap:2px">
          <div class="photo" role="img" aria-label="Glowing digital globe with network lines" style="width:110px;height:54px;background:linear-gradient(135deg,#0a2a5c,#4f8fd0 60%,#0b1e44)"></div>
          <div class="photo" role="img" aria-label="Hands holding a glowing world globe" style="width:118px;height:54px;background:radial-gradient(circle at 50% 45%,#7fb8e6,#2b5f96 45%,#5a2a20 90%)"></div>
          <div class="photo" role="img" aria-label="Silhouettes of business people holding hands against a sky" style="width:146px;height:54px;background:linear-gradient(180deg,#cfe3f6,#4f8fd0 55%,#0b2f6b)"></div>
        </div>
        <div class="section-title" style="margin:6px 0 0 -12px;width:130px">Community</div>
        <div class="body-copy" style="margin-top:5px;width:196px">
          <p>There are many issues that impact all areas of our community. These issues have many causes which in turn can impact many other areas of the community such as:-</p>
          <ul style="padding-left:4px">
            <li>Homelessness</li><li>Mental Health</li><li>Judicial System</li><li>Welfare System</li><li>Elderly Community</li><li>Indigenous Community</li><li>Juveniles and many others</li>
          </ul>
        </div>
      </div>
      <div class="contact">
        <div class="contact__title">CONTACT</div>
        <b>Tessaro World Services Pty Ltd</b><br>
        PO Box 418, Harbour Lane East, Victoria 8102,<br>
        AUSTRALIA<br>
        Tel: +61 (0)3 5550 2148<br>
        info@tessaroworldservices.com
      </div>
      <svg class="band" style="top:400px" width="392" height="50" viewBox="0 0 392 50" aria-hidden="true">
        <path d="M0 26C120 26 200 20 260 8C300 0 340 0 392 0V50H0Z" fill="var(--sky)" opacity=".7"/>
        <path d="M0 30C120 30 220 26 280 14C320 6 360 6 392 6V50H0Z" fill="var(--navy)"/>
      </svg>
      <div class="url" style="left:12px;top:433px">www.tessaroworldservices.com</div>
    </div>

    <div class="page page--right">
      <svg class="band" style="top:0" width="392" height="90" viewBox="0 0 392 90" aria-hidden="true">
        <path d="M0 0H392V8H0Z" fill="var(--deep)"/>
        <path d="M0 48H392V62H0Z" fill="var(--navy)"/>
        <path d="M0 62H392V66H0Z" fill="var(--sky)"/>
      </svg>
      <div class="brand" style="left:150px;top:10px;width:130px">
        <span class="brand__mark" style="width:22px;height:22px"></span>
        <span class="brand__name" style="font-size:11px;margin-top:2px">TESSARO</span>
        <span class="brand__tag" style="font-size:5px">WORLD SERVICES</span>
      </div>
      <div role="img" aria-label="Glowing digital world map made of light points and binary code" style="position:absolute;left:0;top:86px;width:392px;height:240px;background:radial-gradient(ellipse at 60% 45%,#8cc6f2,#2a6fb8 35%,#0b2f6b 65%,#061430)"></div>
      <svg class="band" style="top:300px" width="392" height="150" viewBox="0 0 392 150" aria-hidden="true">
        <defs><linearGradient id="coverBase" x1="0" y1="0" x2="0" y2="1"><stop offset="0" stop-color="#2c78c4"/><stop offset="1" stop-color="#061a3f"/></linearGradient></defs>
        <path d="M0 30C80 10 150 40 240 36C300 33 350 24 392 24V150H0Z" fill="var(--ice)"/>
        <path d="M0 38C80 20 150 48 240 44C300 41 350 32 392 32V150H0Z" fill="url(#coverBase)"/>
        <path d="M0 108C100 104 160 96 260 92C320 90 360 96 392 100V150H0Z" fill="var(--navy)"/>
      </svg>
      <div class="tagline" style="left:196px;top:355px;width:192px">Specialists in Transformational Change &amp; Sustainable Solutions</div>
      <div class="url" style="left:24px;top:433px">www.tessaroworldservices.com</div>
    </div>
  </section>

  <!-- Inner spread -->
  <section class="spread spread--inner">
    <div class="page page--left">
      <svg class="band" style="top:0" width="392" height="30" viewBox="0 0 392 30" aria-hidden="true">
        <path d="M0 0H392V10H0Z" fill="var(--navy)"/>
        <path d="M0 10H392V13H0Z" fill="var(--sky)"/>
      </svg>
      <div class="brand" style="left:8px;top:18px;width:60px">
        <span class="brand__mark" style="width:13px;height:13px"></span>
        <span class="brand__name" style="font-size:6.5px;margin-top:2px">TESSARO</span>
        <span class="brand__tag" style="font-size:3.6px">WORLD SERVICES</span>
      </div>
      <div class="flow" style="left:20px;top:64px;width:356px">
        <div class="headline">Specialists in Transformational<br>Change &amp; Sustainable Solutions</div>
        <div class="row" style="margin-top:6px">
          <div class="body-copy" style="width:190px">
            <p>To succeed in an increasingly competitive and rapidly changing global market and environment, a new way of thinking and design is required. Tessaro World Services brings a dynamic and leading edge approach to support our clients needs. We work across a broad sector supporting the changes required to excel in the 21st Century. We believe in partnering with our clients to develop sustainable solutions that support transition from the current state to the future state.</p>
          </div>
          <div class="photo" role="img" aria-label="Hand placing a puzzle piece against a blue sky and green field" style="width:92px;height:62px;background:linear-gradient(180deg,#9cc8ee,#d8ecfa 55%,#7fb04a)"></div>
        </div>
        <div class="section-title" style="margin:5px 0 0 -14px">Banking &amp; Finance</div>
        <div class="body-copy" style="margin-top:5px">
          <p>Our specialist team has extensive experience across all areas within Banking &amp;Financial Services Whether you are optimising or transforming an existing business or creating something totally new we can assist.</p>
          <p>Many of our models and systems have been designed specifically for this industry. They support all elements of business including</p>
        </div>
        <div class="row" style="justify-content:space-between;align-items:center">
          <div class="body-copy">
            <ul style="padding-left:4px">
              <li>Increasing customer satisfaction</li><li>Enhancing employee satisfaction</li><li>Improving revenue</li><li>Reducing cost</li>
            </ul>
            <p>Our approach to solutions is based on</p>
          </div>
          <div class="photo" role="img" aria-label="Blue financial data screen and graph" style="width:72px;height:46px;margin-right:60px;background:linear-gradient(135deg,#0b2f6b,#3f93db 55%,#0a2350)"><span class="photo-label">Banking &amp; Finance Services</span></div>
        </div>
        <div class="body-copy" style="margin-top:3px">
          <ul>
            <li>A multi-dimensional view of the business</li>
            <li>Understanding the "whole" system to ensure all impacts are managed</li>
            <li>The belief that everything is connected and therefore ALL need to be accounted for within the change</li>
            <li>Ensuring the People and Customer element is understood and supported throughout the transition.</li>
          </ul>
          <p style="margin-top:4px">We are different because</p>
          <ul style="margin-top:4px">
            <li>We specialise in working with ambiguity and complexity</li>
            <li>We challenge current thinking and paradigms</li>
          </ul>
        </div>
      </div>
      <svg class="band" style="top:400px" width="392" height="50" viewBox="0 0 392 50" aria-hidden="true">
        <path d="M0 22C140 22 250 20 320 10C350 6 372 4 392 4V50H0Z" fill="var(--sky)" opacity=".7"/>
        <path d="M0 26C140 26 260 24 330 14C360 10 378 10 392 10V50H0Z" fill="var(--navy)"/>
      </svg>
      <div class="url" style="left:12px;top:433px">www.tessaroworldservices.com</div>
    </div>

    <div class="page page--right">
      <svg class="band" style="top:0" width="392" height="40" viewBox="0 0 392 40" aria-hidden="true">
        <path d="M0 18C60 18 90 4 150 4H392V14H160C100 14 70 26 0 26Z" fill="var(--sky)" opacity=".6"/>
        <path d="M0 0H392V6H0Z" fill="var(--deep)"/>
        <path d="M150 14H392V22H160Z" fill="var(--navy)"/>
      </svg>
      <div class="brand" style="left:330px;top:8px;width:56px">
        <span class="brand__mark" style="width:13px;height:13px"></span>
        <span class="brand__name" style="font-size:6.5px;margin-top:2px">TESSARO</span>
        <span class="brand__tag" style="font-size:3.6px">WORLD SERVICES</span>
      </div>
      <div class="flow" style="left:40px;top:56px;width:330px">
        <div class="section-title section-title--box" style="margin-left:4px">Business</div>
        <div class="body-copy" style="margin-top:7px">
          <p>Our specialist team has extensive experience across all areas of Business.</p>
          <p style="margin-top:4px">Whether you are optimising or transforming an existing business or creating something totally new we can assist.</p>
          <p style="margin-top:4px">Many of our models and systems have been designed specifically for this industry. They support all elements of business including</p>
          <ul style="margin-top:4px;padding-left:4px">
            <li>Increasing customer satisfaction</li><li>Enhancing employee satisfaction</li><li>Improving revenue</li><li>Reducing cost</li>
          </ul>
          <p>Our approach to solutions is based on:</p>
          <ul>
            <li>A multi-dimensional view of the business</li>
            <li>Understanding the "whole" system to ensure all impacts are managed</li>
            <li>The belief that everything is connected and therefore ALL need to be accounted for within the change</li>
            <li>Ensuring the People and Customer element is understood and supported throughout the transition.</li>
          </ul>
        </div>
        <div class="row" style="margin-top:4px;gap:0">
          <div class="photo" role="img" aria-label="Earth glowing over a city skyline at dusk" style="width:92px;height:62px;background:linear-gradient(180deg,#2a6fb8,#0b2f6b 60%,#061430)"><span class="photo-label">Business Solutions</span></div>
          <div class="photo" role="img" aria-label="Team of business professionals in suits" style="width:88px;height:62px;background:linear-gradient(180deg,#f4f7fb,#c9d6e4 70%,#3b4656)"></div>
          <div class="photo" role="img" aria-label="Globe held in a hand on a blue background" style="width:82px;height:62px;background:radial-gradient(circle at 50% 50%,#8cc6f2,#1b5fae 50%,#071d45)"></div>
        </div>
        <div class="section-title section-title--box" style="margin:6px 0 0 4px">Global Solution</div>
        <div class="body-copy" style="margin-top:6px">
          <p>There are many issues that impact all areas of our Global community.</p>
          <p style="margin-top:4px">To create sustainable solutions all aspects of the Global system need to be understood and managed as a 'whole' system.Tessaro World Services specialise in working with complex problems that are multi-layered and have multiple interdependencies.</p>
        </div>
      </div>
      <svg class="band" style="top:400px" width="392" height="50" viewBox="0 0 392 50" aria-hidden="true">
        <path d="M0 30C60 28 110 10 200 8C290 6 340 8 392 8V50H0Z" fill="var(--sky)" opacity=".7"/>
        <path d="M0 34C60 32 120 16 210 14C300 12 350 14 392 14V50H0Z" fill="var(--navy)"/>
      </svg>
      <div class="url" style="left:262px;top:428px">www.tessaroworldservices.com</div>
    </div>
  </section>

</div>
</body>
</html>
```